Looking for awesome business card design with attached existing logo

We are a water, mold, and fire damage restoration company called "Solvane Crest" Looking for an awesome business card that is edgy yet professional and unique. Show me what you got!

```html
<!DOCTYPE html>
<html lang="en">
<head>
<meta charset="utf-8">
<title>Solvane Crest — Business Card</title>
<link href="https://fonts.googleapis.com/css2?family=Montserrat:wght@400;500;700;800&display=swap" rel="stylesheet">
<style>
  :root {
    --stage: #8a8a88;
    --paper: #fbfbf9;
    --navy: #1f3d4f;
    --teal-dark: #2c4a58;
    --teal-light: #3f6a7c;
    --gold: #d9921f;
    --red: #c8283a;
    --ink-soft: #555a5e;
  }
  * { box-sizing: border-box; margin: 0; padding: 0; }
  html, body { width: 1200px; height: 801px; overflow: hidden; }
  body {
    background: var(--stage);
    font-family: "Montserrat", sans-serif;
    display: flex;
    align-items: center;
    justify-content: center;
    gap: 40px;
  }
  .card {
    width: 540px;
    height: 309px;
    position: relative;
    border-bottom: 3px solid var(--gold);
    box-shadow: 0 10px 24px rgba(0,0,0,.25);
  }
  .card--front { background: var(--paper); }
  .card--back { background: var(--teal-dark); }

  .brand {
    position: absolute;
    left: 36px;
    top: 72px;
    display: flex;
    align-items: center;
    gap: 12px;
  }
  .brand__dot { width: 18px; height: 18px; border-radius: 50%; background: var(--gold); }
  .brand__name {
    font-weight: 800;
    font-size: 30px;
    line-height: 1.05;
    color: var(--navy);
    text-transform: uppercase;
    letter-spacing: 1px;
  }

  .person {
    position: absolute;
    right: 34px;
    top: 60px;
    text-align: right;
  }
  .person__name {
    font-weight: 800;
    font-size: 19px;
    color: var(--navy);
    letter-spacing: .5px;
  }
  .person__role {
    font-weight: 500;
    font-size: 13px;
    color: var(--gold);
    margin-top: 2px;
  }

  .divider {
    position: absolute;
    left: 36px;
    right: 34px;
    top: 168px;
    height: 1px;
    background: var(--gold);
  }

  .contacts {
    position: absolute;
    left: 36px;
    top: 186px;
    list-style: none;
    font-size: 13px;
    color: var(--ink-soft);
  }
  .contacts li { display: flex; align-items: center; gap: 9px; line-height: 22px; }
  .contacts svg { width: 12px; height: 12px; flex: none; }

  .address {
    position: absolute;
    right: 34px;
    top: 186px;
    text-align: right;
    font-style: normal;
    font-size: 13px;
    line-height: 22px;
    color: var(--ink-soft);
  }

  .pattern {
    position: absolute;
    inset: 0;
    background: linear-gradient(135deg, var(--teal-dark) 0%, var(--teal-dark) 55%, var(--teal-light) 100%);
  }
  .back-brand {
    position: absolute;
    right: 70px;
    top: 128px;
    display: flex;
    align-items: center;
    gap: 10px;
  }
  .back-brand__name {
    font-weight: 800;
    font-size: 16px;
    color: var(--gold);
    text-transform: uppercase;
    letter-spacing: 1px;
  }
</style>
</head>
<body>
  <section class="card card--front" aria-label="Business card front">
    <div class="brand">
      <span class="brand__dot"></span>
      <span class="brand__name">Solvane<br>Crest</span>
    </div>

    <div class="person">
      <div class="person__name">MARCUS TRELL</div>
      <div class="person__role">President</div>
    </div>

    <div class="divider"></div>

    <ul class="contacts">
      <li>
        <svg viewBox="0 0 24 24" fill="var(--red)"><path d="M6.6 10.8a15.1 15.1 0 0 0 6.6 6.6l2.2-2.2a1 1 0 0 1 1-.25 11.4 11.4 0 0 0 3.6.57 1 1 0 0 1 1 1V20a1 1 0 0 1-1 1A17 17 0 0 1 3 4a1 1 0 0 1 1-1h3.5a1 1 0 0 1 1 1c0 1.25.2 2.45.57 3.57a1 1 0 0 1-.25 1z"/></svg>
        555-014-3827
      </li>
      <li>
        <svg viewBox="0 0 24 24" fill="var(--red)"><path d="M2 5h20v14H2z"/><path d="M2 5l10 8 10-8" fill="none" stroke="#fff" stroke-width="2"/></svg>
        marcustrell@solvanecrest.com
      </li>
      <li>
        <svg viewBox="0 0 24 24"><circle cx="12" cy="12" r="10" fill="var(--red)"/><path d="M2 12h20M12 2c3 3 3 17 0 20M12 2c-3 3-3 17 0 20" fill="none" stroke="#fff" stroke-width="1.5"/></svg>
        www.solvanecrest.com
      </li>
    </ul>

    <address class="address">
      18420 Harbor Crest Way<br>
      Bayview CA 90000
    </address>
  </section>

  <section class="card card--back" aria-label="Business card back">
    <div class="pattern" role="img" aria-label="Embossed repeating brand symbol pattern in dark and light teal"></div>
    <div class="back-brand">
      <span class="brand__dot"></span>
      <span class="back-brand__name">Solvane Crest</span>
    </div>
  </section>
</body>
</html>
```